Website Design for Employee Moral and Happiness Company

Looking for a clean website design that explains our features in a step by step manner so our visitors know exactly what our site does before logging in.

The site is called "Velquo". See logo design and video for a sample of style and an overview of what we do.

Target Market(s)

Business owners that are looking to retain employees.

Number of Pages Required

1 page

```html
<!DOCTYPE html>
<html lang="en">
<head>
<meta charset="utf-8">
<title>Velquo – Employee Morale &amp; Happiness</title>
<link rel="stylesheet" href="https://fonts.googleapis.com/css2?family=Jost:wght@400;500;600;700&display=swap">
<style>
:root{
  --orange:#f26b1d;
  --orange-deep:#ee4f14;
  --orange-light:#ff9a1f;
  --ink:#1b1b1b;
  --body:#555;
  --muted:#8a8a8a;
  --hero-bg:#f3f3f3;
  --line:#e3e3e3;
  --footer:#0c0c0c;
  --footer-bar:#1d1d1d;
  --star:#f7b500;
}
*{margin:0;padding:0;box-sizing:border-box}
html,body{width:1200px;height:4622px;overflow:hidden}
body{position:relative;background:#fff;font-family:'Jost',sans-serif;color:var(--ink)}
.abs{position:absolute}
.accent{color:var(--orange)}
.logo{font-family:'Jost',sans-serif;font-weight:700;letter-spacing:.5px}
.nav .logo{left:110px;top:12px;font-size:48px;color:#111}
.nav-link{top:34px;font-size:15px;color:#444}
.nav-link.active{color:var(--orange)}
.nav-link.active::after{content:"";position:absolute;left:50%;top:24px;width:22px;height:6px;margin-left:-11px;border:3px solid var(--orange);border-top:none;border-radius:0 0 14px 14px}
.btn-outline{display:flex;align-items:center;justify-content:center;border:2px solid var(--orange);border-radius:30px;color:var(--orange);font-size:17px;font-weight:500;background:#fff}
.btn-fill{display:flex;align-items:center;justify-content:center;border-radius:30px;color:#fff;font-size:17px;font-weight:500;background:linear-gradient(90deg,var(--orange-light),var(--orange-deep))}
.nav-contact{left:978px;top:27px;width:124px;height:36px;font-size:14px}
.nav-rule{left:0;top:83px;width:1200px;height:1px;background:var(--line)}
.hero-title{left:113px;top:262px;font-size:40px;line-height:45px;font-weight:500}
.hero-title .accent{font-weight:600}
.para{font-size:14px;line-height:28px;color:var(--body)}
.illus{border-radius:18px}
.feature-card{background:#fff;border-radius:8px;box-shadow:0 10px 30px rgba(0,0,0,.08);padding:30px 28px}
.feature-card h4{font-size:16px;line-height:20px;font-weight:600;margin:16px 0 12px}
.feature-card p{font-size:11px;line-height:15px;color:var(--muted)}
.feature-card.hot{background:linear-gradient(135deg,var(--orange-light),var(--orange-deep));color:#fff}
.feature-card.hot p{color:#ffe3cf}
.card-icon{width:42px;height:42px}
.dots{background-image:radial-gradient(var(--orange) 1.6px,transparent 1.8px);background-size:16px 16px;opacity:.55}
.section-title{font-size:43px;font-weight:500}
.section-title .accent{font-weight:600}
.centered{width:1200px;left:0;text-align:center}
.underline{left:585px;width:30px;height:4px;background:var(--orange);border-radius:2px}
.item-title{font-size:32px;font-weight:500}
.connector{fill:none;stroke:#d9d9d9;stroke-width:1.5}
.boost h2{font-size:37px;line-height:38px;font-weight:500;color:#fff}
.boost p{font-size:16px;line-height:27px;color:#fff}
.quote{background:#fff;border:1px solid #e5e5e5;border-radius:6px;padding:34px 36px}
.quote p{font-size:12.5px;line-height:23px;color:#666;font-style:italic}
.quote h5{font-size:13px;font-weight:600;margin:12px 0 6px}
.stars{color:var(--star);font-size:19px;letter-spacing:5px}
.arrow{font-size:40px;color:#ccc;font-weight:300}
.cta{left:111px;top:4028px;width:985px;height:206px;border-radius:10px;background:linear-gradient(90deg,var(--orange-light),var(--orange-deep))}
.cta h3{position:absolute;left:50px;top:72px;font-size:36px;line-height:38px;font-weight:500;color:#fff}
.cta-btn{left:716px;top:77px;width:178px;height:46px;background:#fff;color:var(--orange);border-radius:30px;font-size:17px;font-weight:500;display:flex;align-items:center;justify-content:center}
.footer{left:0;top:4159px;width:1200px;height:463px;background:var(--footer)}
.footer .logo{color:#fff}
.foot-head{font-size:20px;font-weight:500;color:#fff}
.foot-link{font-size:13px;color:#cfcfcf}
.foot-text{font-size:12px;line-height:18px;color:#b5b5b5}
.social{width:26px;height:26px;border-radius:50%}
.footer-bar{left:0;top:4557px;width:1200px;height:65px;background:var(--footer-bar);text-align:center;font-size:11px;color:#9a9a9a;line-height:65px}
</style>
</head>
<body>

<!-- Hero background -->
<svg class="abs" style="left:0;top:84px" width="1200" height="660" aria-hidden="true">
  <defs><linearGradient id="heroGrad" x1="0" y1="0" x2="0" y2="1"><stop offset="0" stop-color="#fff"/><stop offset="1" stop-color="#ededed"/></linearGradient></defs>
  <path d="M0 0 H1200 V470 Q620 740 0 500 Z" fill="url(#heroGrad)"/>
  <path d="M262 592 Q600 690 948 586" fill="none" stroke="var(--orange)" stroke-width="5" stroke-linecap="round"/>
</svg>

<!-- Navigation -->
<header class="nav">
  <div class="abs logo">Velquo</div>
  <a class="abs nav-link active" style="left:386px">About Us</a>
  <a class="abs nav-link" style="left:502px">Our Services</a>
  <a class="abs nav-link" style="left:646px">How it work</a>
  <a class="abs nav-link" style="left:780px">Why Us</a>
  <a class="abs nav-link" style="left:886px">Blogs</a>
  <a class="abs btn-outline nav-contact">Contact Us</a>
  <div class="abs nav-rule"></div>
</header>

<!-- Hero -->
<section class="hero">
  <h1 class="abs hero-title">Velquo is here to help<br><span class="accent">Businesses like yours</span></h1>
  <p class="abs para" style="left:113px;top:370px;width:400px;line-height:20px">Lorem Ipsum is simply dummy text of the printing and typesetting industry. Lorem Ipsum has been.</p>
  <a class="abs btn-fill" style="left:113px;top:443px;width:178px;height:45px">Get Started &gt;</a>
  <div class="abs illus" role="img" aria-label="Illustration of a woman working on a laptop surrounded by plants, mail, chat and calendar icons" style="left:583px;top:170px;width:475px;height:440px;background:radial-gradient(circle at 50% 55%,#fbd9c3 0%,#e6efee 45%,rgba(255,255,255,0) 72%)"></div>
</section>

<!-- About -->
<section class="about">
  <div class="abs dots" style="left:106px;top:772px;width:120px;height:100px"></div>
  <div class="abs dots" style="left:480px;top:1122px;width:110px;height:20px"></div>
  <div class="abs feature-card" style="left:135px;top:798px;width:211px;height:201px">
    <svg class="card-icon" viewBox="0 0 42 42" fill="none" stroke="var(--orange)" stroke-width="2"><circle cx="15" cy="24" r="8"/><circle cx="15" cy="24" r="3"/><circle cx="30" cy="12" r="6"/><circle cx="30" cy="12" r="2"/></svg>
    <h4>Manage Your Business</h4>
    <p>Lorem Ipsum is simply dummy text of the printing</p>
  </div>
  <div class="abs feature-card hot" style="left:368px;top:908px;width:213px;height:206px">
    <svg class="card-icon" viewBox="0 0 42 42" fill="none" stroke="#fff" stroke-width="2"><path d="M4 38H38"/><path d="M9 36V26M16 36V20M23 36V24M30 36V16"/><path d="M6 22L15 13L22 19L36 6"/></svg>
    <h4>Increase Employee Retention</h4>
    <p>Lorem Ipsum is simply dummy text of the printing</p>
  </div>
  <div class="abs feature-card" style="left:135px;top:1028px;width:211px;height:204px">
    <svg class="card-icon" viewBox="0 0 42 42" fill="none" stroke="var(--orange)" stroke-width="2"><rect x="5" y="8" width="32" height="28" rx="2"/><path d="M5 16H37M13 4V11M29 4V11M12 22H16M19 22H23M26 22H30M12 29H16M19 29H23"/></svg>
    <h4>Event Manage &amp; Planning</h4>
    <p>Lorem Ipsum is simply dummy text of the printing</p>
  </div>
  <h2 class="abs section-title" style="left:649px;top:832px">About <span class="accent">Velquo</span></h2>
  <p class="abs para" style="left:650px;top:925px;width:465px">Lorem Ipsum is simply dummy text of the printing and typesetting industry. Lorem Ipsum has been the industry's standard dummy text ever since the 1500s, when an unknown.</p>
  <p class="abs para" style="left:650px;top:1029px;width:465px">printer took a galley of type and scrambled it to make a type specimen book. It has survived not only five centuries, but also the leap into electronic typesetting, remaining essentially</p>
  <a class="abs btn-outline" style="left:646px;top:1143px;width:179px;height:50px">Learn More</a>
</section>

<!-- What we do -->
<section class="services">
  <h2 class="abs section-title centered" style="top:1316px">What <span class="accent">We Do</span></h2>
  <div class="abs underline" style="top:1373px"></div>

  <h3 class="abs item-title" style="left:133px;top:1497px">Increase Employee <span class="accent">Retention</span></h3>
  <p class="abs para" style="left:133px;top:1561px;width:450px">Lorem Ipsum is simply dummy text of the printing and typesetting industry. Lorem Ipsum has been the industry's standard dummy text ever since the 1500s, when an nknown.</p>
  <p class="abs para" style="left:133px;top:1662px;width:450px">printer took a galley of type and scrambled it to make a type specimen book. m Ipsum is simply dummy text</p>
  <a class="abs btn-outline" style="left:131px;top:1749px;width:178px;height:45px">Learn More</a>
  <div class="abs illus" role="img" aria-label="Illustration of a man working at a desk with a progress bar, clock and notes" style="left:682px;top:1435px;width:376px;height:377px;background:linear-gradient(160deg,#fff 0%,#f1f1f3 55%,#fde3d2 100%)"></div>

  <svg class="abs" style="left:0;top:1860px" width="1200" height="620" aria-hidden="true">
    <path class="connector" d="M763 0 V50 Q763 78 735 78 H520 Q493 78 493 106 V200"/>
    <path class="connector" d="M485 505 V540 Q485 576 513 576 H727 Q753 576 753 604 V620"/>
  </svg>

  <div class="abs illus" role="img" aria-label="Illustration of a man beside a large planner calendar with gears, clock, books and pencil" style="left:108px;top:1964px;width:412px;height:386px;background:radial-gradient(ellipse at 50% 70%,#ececec 0%,#f6f6f6 50%,rgba(255,255,255,0) 72%)"></div>
  <h3 class="abs item-title" style="left:617px;top:2022px">Easy Event <span class="accent">Plnning</span></h3>
  <p class="abs para" style="left:618px;top:2085px;width:460px">Lorem Ipsum is simply dummy text of the printing and typesetting industry. Lorem Ipsum has been the industry's standard dummy text ever since the 1500s, when an nknown.</p>
  <p class="abs para" style="left:618px;top:2186px;width:460px">printer took a galley of type and scrambled it to make a type specimen book. m Ipsum is simply dummy text</p>
  <a class="abs btn-outline" style="left:615px;top:2270px;width:180px;height:53px">Learn More</a>

  <h3 class="abs item-title" style="left:138px;top:2512px">From Raffles to <span class="accent">Auctions</span></h3>
  <p class="abs para" style="left:139px;top:2575px;width:450px">Lorem Ipsum is simply dummy text of the printing and typesetting industry. Lorem Ipsum has been the industry's standard dummy text ever since the 1500s, whe an nknown. printer took a galley of type and scrambled it to make a type specimen book. m Ipsum is simply dummy text</p>
  <a class="abs btn-outline" style="left:136px;top:2739px;width:180px;height:51px">Learn More</a>
  <div class="abs illus" role="img" aria-label="Illustration of a laptop with a bid sign and ticket, and a woman on a stool with a coin icon" style="left:628px;top:2449px;width:430px;height:403px;background:radial-gradient(ellipse at 50% 60%,#fde1cf 0%,#f3f3f3 45%,rgba(255,255,255,0) 72%)"></div>
</section>

<!-- Boost band -->
<section class="boost">
  <svg class="abs" style="left:0;top:2860px" width="1200" height="656" aria-hidden="true">
    <defs><linearGradient id="bandGrad" x1="0" y1="0" x2="1" y2="0"><stop offset="0" stop-color="var(--orange-light)"/><stop offset="1" stop-color="var(--orange-deep)"/></linearGradient></defs>
    <path d="M0 22 C240 110 520 90 760 60 S1080 20 1200 50 V656 H0 Z" fill="url(#bandGrad)"/>
  </svg>
  <h2 class="abs centered" style="top:3008px">Boost employee morale<br>and transform <span style="border-bottom:3px solid #fff">your</span> work events</h2>
  <p class="abs centered" style="top:3112px">Lorem Ipsum is simply dummy text of the printing and typesetting<br>industry. Lorem Ipsum has been the industry's standard</p>
  <div class="abs" role="img" aria-label="Illustration of a man working on a laptop with floating mail, chat and calendar icons" style="left:233px;top:3211px;width:790px;height:305px;background:linear-gradient(180deg,rgba(255,255,255,0) 0%,rgba(255,214,180,.35) 40%,rgba(40,60,110,.35) 100%);border-radius:20px 20px 0 0"></div>
</section>

<!-- Testimonials -->
<section class="testimonials">
  <h2 class="abs centered" style="top:3598px;font-size:34px;font-weight:500">What <span class="accent">Our Client Says</span></h2>
  <span class="abs arrow" style="left:70px;top:3776px">‹</span>
  <span class="abs arrow" style="left:1118px;top:3776px">›</span>
  <div class="abs quote" style="left:111px;top:3690px;width:318px;height:226px">
    <p>Lorem Ipsum is simply dummy text of the printing and typesetting industry. Lorem Ipsum has been the industry's standard dummy text ever since the 1500s, when an unknown printer took a galley</p>
    <h5>Marlow Denton</h5><div class="stars">★★★★★</div>
  </div>
  <div class="abs quote" style="left:447px;top:3690px;width:315px;height:226px">
    <p>Lorem Ipsum is simply dummy text of the printing and typesetting industry. Lorem Ipsum has been the industry's standard dummy text ever since the 1500s, when an unknown printer took a galley</p>
    <h5>Marlow Denton</h5><div class="stars">★★★★★</div>
  </div>
  <div class="abs quote" style="left:780px;top:3690px;width:318px;height:226px">
    <p>Lorem Ipsum is simply dummy text of the printing and typesetting industry. Lorem Ipsum has been the industry's standard dummy text ever since the 1500s, when an unknown printer took a galley</p>
    <h5>Marlow Denton</h5><div class="stars">★★★★★</div>
  </div>
</section>

<!-- Footer -->
<footer>
  <div class="abs footer">
    <div class="abs logo" style="left:115px;top:150px;font-size:48px">Velquo</div>
    <p class="abs foot-text" style="left:117px;top:232px;width:240px">Lorem Ipsum is simply dummy text of the printing and typesetting industry. Lorem Ipsum has been.</p>
    <h4 class="abs foot-head" style="left:465px;top:162px">Navigation</h4>
    <a class="abs foot-link" style="left:468px;top:205px">About Us</a>
    <a class="abs foot-link" style="left:468px;top:233px">What We Do</a>
    <a class="abs foot-link" style="left:468px;top:261px">Our Services</a>
    <a class="abs foot-link" style="left:468px;top:290px">Why Us</a>
    <h4 class="abs foot-head" style="left:700px;top:162px">Resources</h4>
    <a class="abs foot-link" style="left:703px;top:205px">Support</a>
    <a class="abs foot-link" style="left:703px;top:233px">Testimonials</a>
    <a class="abs foot-link" style="left:703px;top:261px">FAQ</a>
    <a class="abs foot-link" style="left:703px;top:290px">Contact Us</a>
    <h4 class="abs foot-head" style="left:921px;top:162px">Stay in touch</h4>
    <span class="abs social" aria-label="Social link" style="left:924px;top:202px;background:var(--orange)"></span>
    <span class="abs social" aria-label="Social link" style="left:956px;top:202px;background:#fff"></span>
    <span class="abs social" aria-label="Social link" style="left:988px;top:202px;background:#fff"></span>
    <span class="abs social" aria-label="Social link" style="left:1020px;top:202px;background:#fff"></span>
  </div>
  <div class="abs footer-bar">© 2022 velquo. All rights reserved &nbsp;|&nbsp; Privacy &nbsp;|&nbsp; Terms of Use</div>
</footer>

<!-- Call to action -->
<section class="abs cta">
  <h3>Start building your<br><b style="font-weight:600">event today with me!</b></h3>
  <a class="abs cta-btn">Get Started &gt;</a>
</section>

</body>
</html>
```